Halvery Metal Recyclers - www.halveryrecyclers.com.au

I've just rebranded my business and thought what better way to continue with this than getting a website.
It is going to be fairly basic for now. I've attached quite a few images, feel free to use whichever you like.
And pages description is also attached in a .doc file.
Updates

Hi, this is my first time having a website. I am open to anything and trust the experience and ideas you can bring forward. I will look at extending the deadline so I can take my time to give feedback as needed! Thank you all.

Target Market(s)

Mining and industrial and commercial sectors

Coding

Coded - Design and coding required

Number of Pages Required

5+ page

Requirements
Must have
• Logo/Phone number at the top of every page. "Scrap Metal Specialists" tag line at the top of every page.
Nice to have
• Top Navigation.

```html
<!DOCTYPE html>
<html lang="en">
<head>
<meta charset="utf-8">
<title>Halvery Metal Recyclers</title>
<link href="https://fonts.googleapis.com/css2?family=Oswald:wght@400;500;700&family=Poppins:ital,wght@0,400;0,500;0,600;1,500&display=swap" rel="stylesheet">
<style>
  :root{
    --blue:#1f3f7a;
    --blue-deep:#17315f;
    --nav-active:#4f8fe8;
    --white:#ffffff;
    --grey:#8b8c90;
    --text:#4a4a4a;
    --heading:#3d3d3d;
    --line:#9a9a9a;
    --store:#8f9094;
  }
  *{box-sizing:border-box;margin:0;padding:0}
  html,body{width:1200px;height:1055px;overflow:hidden;background:var(--white)}
  body{position:relative;font-family:'Poppins',sans-serif}

  .hero{position:absolute;left:0;top:0;width:1200px;height:711px;overflow:hidden}
  .hero-photo{position:absolute;inset:0;
    background:radial-gradient(ellipse at 75% 55%,#9a6a33 0%,#5d4227 35%,#2c2520 70%,#1b1a1c 100%)}
  .hero-panel{position:absolute;inset:0}

  .brand{position:absolute;left:111px;top:30px;color:var(--white);
    font-family:'Oswald',sans-serif;font-weight:700;font-size:40px;line-height:1.05;letter-spacing:1px;text-transform:uppercase;width:260px}
  .tagline{position:absolute;left:393px;top:70px;color:var(--white);
    font-style:italic;font-weight:500;font-size:26px;line-height:31px}

  .topbar{position:absolute;right:113px;top:23px;color:var(--white);font-size:15px;display:flex;align-items:center;gap:8px}
  .topbar svg{width:13px;height:13px;fill:var(--white);vertical-align:-1px;margin-right:3px}

  .main-nav{position:absolute;right:112px;top:62px;display:flex;align-items:center;gap:17px;
    font-family:'Oswald',sans-serif;font-size:20px;text-transform:uppercase}
  .main-nav a{color:var(--white);text-decoration:none}
  .main-nav a.is-active{color:var(--nav-active)}
  .main-nav a.store{background:var(--store);padding:3px 8px;margin-left:2px}

  .hero-title{position:absolute;left:107px;top:215px;color:var(--white);
    font-family:'Oswald',sans-serif;font-weight:700;font-size:57px;line-height:65px;text-transform:uppercase}
  .hero-copy{position:absolute;left:108px;top:368px;width:370px;color:var(--white);font-size:19px;line-height:28.3px}
  .btn-shop{position:absolute;left:111px;top:572px;width:206px;height:64px;border-radius:32px;background:var(--white);
    color:#222;font-weight:600;font-size:20px;display:flex;align-items:center;justify-content:center}

  .footer-brand{position:absolute;left:108px;top:790px;width:330px;color:var(--grey);
    font-family:'Oswald',sans-serif;font-weight:700;font-size:48px;line-height:1.05;text-transform:uppercase}
  .footer-col h3{font-size:19px;font-weight:500;color:var(--heading);margin-bottom:18px}
  .quick-links{position:absolute;left:536px;top:766px}
  .quick-links a{display:block;color:var(--text);text-decoration:none;font-size:17px;line-height:27.5px}
  .contact-us{position:absolute;left:716px;top:766px}
  .contact-row{display:flex;align-items:center;gap:8px;color:var(--text);font-size:17px;margin-bottom:19px}
  .contact-row .ic{width:36px;height:36px;border:1.5px solid var(--blue-deep);border-radius:50%;display:flex;align-items:center;justify-content:center}
  .contact-row .ic svg{width:16px;height:16px;fill:var(--blue-deep)}
  .contact-row span{position:relative;top:-8px}
  .rule{position:absolute;left:111px;top:977px;width:977px;height:1px;background:var(--line)}
  .copyright{position:absolute;left:110px;top:1003px;color:var(--text);font-size:17px}
  .social{position:absolute;left:907px;top:996px;display:flex;gap:7px}
  .social span{width:41px;height:41px;border:1.5px solid var(--blue-deep);border-radius:50%}
</style>
</head>
<body>
<header class="hero">
  <div class="hero-photo" role="img" aria-label="Photo of large rusted steel cable drums and scrap metal in a yard at night"></div>
  <svg class="hero-panel" width="1200" height="711" viewBox="0 0 1200 711">
    <polygon points="0,0 682,0 405,711 0,711" fill="var(--blue)" opacity="0.92"/>
  </svg>

  <div class="brand">Halvery Metal Recyclers</div>
  <div class="tagline">Scrap Metal<br>Specialists</div>

  <div class="topbar">
    <span><svg viewBox="0 0 24 24"><path d="M6.6 10.8a15 15 0 0 0 6.6 6.6l2.2-2.2c.3-.3.7-.4 1-.2 1.1.4 2.3.6 3.6.6.6 0 1 .4 1 1V20c0 .6-.4 1-1 1A17 17 0 0 1 3 4c0-.6.4-1 1-1h3.5c.6 0 1 .4 1 1 0 1.3.2 2.5.6 3.6.1.3 0 .7-.2 1z"/></svg>0491502736</span>
    <span>|</span>
    <span><svg viewBox="0 0 24 24"><path d="M2 5h20v2l-10 6L2 7z M2 9l10 6 10-6v10H2z"/></svg>tom@halveryrecyclers.com.au</span>
  </div>

  <nav class="main-nav">
    <a class="is-active" href="#">Home</a>
    <a href="#">About</a>
    <a href="#">Services</a>
    <a href="#">Blog</a>
    <a href="#">Contact</a>
    <a class="store" href="#">Store</a>
  </nav>

  <h1 class="hero-title">Halvery<br>Metal Recycler</h1>
  <p class="hero-copy">Welcome to the website of Halvery Metal Recyclers. We are a Perth based company that provides scrap metal collection and oxy cutting services in the mining, construction, and industrial sectors all around WA.</p>
  <a class="btn-shop">SHOP NOW</a>
</header>

<footer>
  <div class="footer-brand">Halvery Metal Recyclers</div>

  <div class="footer-col quick-links">
    <h3>Quick Links</h3>
    <a href="#">Home</a>
    <a href="#">About</a>
    <a href="#">Services</a>
    <a href="#">Blog</a>
    <a href="#">Contact</a>
  </div>

  <div class="footer-col contact-us">
    <h3>Contact Us</h3>
    <div class="contact-row">
      <div class="ic"><svg viewBox="0 0 24 24"><path d="M6.6 10.8a15 15 0 0 0 6.6 6.6l2.2-2.2c.3-.3.7-.4 1-.2 1.1.4 2.3.6 3.6.6.6 0 1 .4 1 1V20c0 .6-.4 1-1 1A17 17 0 0 1 3 4c0-.6.4-1 1-1h3.5c.6 0 1 .4 1 1 0 1.3.2 2.5.6 3.6.1.3 0 .7-.2 1z"/></svg></div>
      <span>Call: 0491502736</span>
    </div>
    <div class="contact-row">
      <div class="ic"><svg viewBox="0 0 24 24"><path d="M2 5h20v2l-10 6L2 7z M2 9l10 6 10-6v10H2z"/></svg></div>
      <span>Email: tom@halveryrecyclers.com.au</span>
    </div>
  </div>

  <div class="rule"></div>
  <p class="copyright">Copyright © 2022, Halvery Metal Recyclers. All rights reserved.</p>
  <div class="social" aria-label="Social links"><span></span><span></span><span></span><span></span></div>
</footer>
</body>
</html>
```